Author and Publisher

Cover for a book on the process of publishing a book from the presentation to the publisher until the selling in bookstores :
A behind-the-scenes journey through the world of book publishing, from manuscript to bookstore. The book explores the relationship between authors and publishers, manuscript selection, contracts, editing, proofreading, book design, printing, distribution, bookstores and online sales. It reveals the many people, decisions and processes involved in turning a text into a physical book and bringing it to readers. The illustration should evoke publishing as a lively, contemporary ecosystem, combining creativity, craftsmanship, business and the enduring appeal of books.
FORMAT : 14 x 20,5 cm
AUTHOR : Luc Varennes
TITLE : Le scribe et la presse
PUBLISHER : Editions Trovel (at the bottom of the page)
Target Market(s)
General public, mainly news authors of books
Look and feel
Each slider illustrates characteristics of the customer's brand and the style your logo design should communicate.

```html
<!DOCTYPE html>
<html lang="fr">
<head>
<meta charset="utf-8">
<title>Le scribe et la presse — Luc Varennes</title>
<link rel="stylesheet" href="https://fonts.googleapis.com/css2?family=Bodoni+Moda:ital,opsz,wght@0,6..96,400;0,6..96,800;1,6..96,800&display=swap">
<style>
  :root {
    --paper: #fcfbf7;
    --ink: #0a0a0a;
    --gold: #b08f48;
  }
  html, body {
    margin: 0;
    padding: 0;
    width: 800px;
    height: 1200px;
    overflow: hidden;
    background: var(--paper);
  }
  .cover {
    display: block;
    width: 800px;
    height: 1200px;
    background: var(--paper);
  }
  .cover text {
    font-family: "Bodoni Moda", "Didot", serif;
    text-anchor: middle;
  }
  .author {
    fill: var(--ink);
    font-size: 52px;
    font-weight: 400;
    letter-spacing: 9px;
  }
  .title-line {
    fill: var(--ink);
    font-size: 160px;
    font-weight: 800;
    letter-spacing: -3px;
  }
  .title-conjunction {
    fill: var(--gold);
    font-size: 160px;
    font-style: italic;
    font-weight: 800;
  }
  .rule {
    stroke: var(--gold);
    stroke-width: 2;
  }
  .subtitle {
    fill: var(--ink);
    font-size: 38px;
    font-weight: 400;
    letter-spacing: 6px;
  }
  .publisher {
    fill: var(--ink);
    font-size: 24px;
    font-weight: 400;
    letter-spacing: 3px;
  }
</style>
</head>
<body>
  <svg class="cover" viewBox="0 0 800 1200" xmlns="http://www.w3.org/2000/svg">
    <text class="author" x="400" y="142">Luc Varennes</text>

    <text class="title-line" x="400" y="440">Le scribe</text>
    <text class="title-conjunction" x="400" y="580">et</text>
    <text class="title-line" x="400" y="752">la presse</text>

    <line class="rule" x1="333" y1="840" x2="464" y2="840"/>
    <text class="subtitle" x="400" y="924">Du manuscrit la librairie</text>
    <line class="rule" x1="333" y1="1036" x2="464" y2="1036"/>

    <text class="publisher" x="400" y="1116">Editions Trovel</text>
  </svg>
</body>
</html>
```